I need a business card design for a real estate finance, development and management business. We deal with high net worth clients and ask that the business card be neat, clean and sophisticated. We like the attached logo design, font and color and want to incorporate all this into the business card.

Industry/Entity Type

Real Estate

```html
<!DOCTYPE html>
<html lang="en">
<head>
<meta charset="utf-8">
<title>Harbor Ridge – Business Card</title>
<link href="https://fonts.googleapis.com/css2?family=Open+Sans:wght@400;600;700&display=swap" rel="stylesheet">
<style>
  :root {
    --stage: #e8e8e8;
    --brand-blue: #21609e;
    --ink-black: #0c0d0f;
    --paper: #ffffff;
    --contact-blue: #2f8fe0;
    --card-shadow: rgba(0, 0, 0, 0.18);
  }
  html, body {
    margin: 0;
    padding: 0;
    width: 1200px;
    height: 947px;
    overflow: hidden;
    background: var(--stage);
    font-family: "Open Sans", Arial, sans-serif;
  }
  .stage {
    position: relative;
    width: 1200px;
    height: 947px;
  }
  .card {
    position: absolute;
    top: 325px;
    width: 520px;
    height: 297px;
    filter: drop-shadow(0 6px 14px var(--card-shadow));
  }
  .card--front { left: 60px; }
  .card--back { left: 620px; }
  .card svg { display: block; }
  .fill-blue { fill: var(--brand-blue); }
  .fill-black { fill: var(--ink-black); }
  .fill-paper { fill: var(--paper); }
  .brand-name {
    font-family: "Open Sans", Arial, sans-serif;
    font-weight: 600;
    letter-spacing: 2px;
  }
  .brand-name--on-blue { fill: var(--paper); font-size: 30px; }
  .brand-name--on-white { fill: var(--brand-blue); font-size: 34px; }
  .contact-text {
    font-family: "Open Sans", Arial, sans-serif;
    font-size: 13px;
    fill: var(--contact-blue);
  }
  .phone-on-white {
    font-family: "Open Sans", Arial, sans-serif;
    font-size: 14px;
    fill: var(--brand-blue);
  }
  .holder-name {
    font-family: "Open Sans", Arial, sans-serif;
    font-size: 17px;
    fill: var(--brand-blue);
    letter-spacing: 0.5px;
  }
  .holder-name .holder-name__last { font-weight: 700; }
  .icon-white { fill: var(--paper); }
  .icon-blue { fill: var(--brand-blue); }
</style>
</head>
<body>
<main class="stage">

  <!-- Front side -->
  <div class="card card--front">
    <svg width="520" height="297" viewBox="0 0 520 297" xmlns="http://www.w3.org/2000/svg">
      <rect class="fill-paper" x="0" y="0" width="520" height="297"/>
      <rect class="fill-blue" x="0" y="0" width="520" height="145"/>
      <rect class="fill-black" x="0" y="205" width="520" height="92"/>

      <text class="brand-name brand-name--on-blue" x="300" y="92" text-anchor="middle">HARBOR RIDGE</text>

      <!-- mobile icon + number -->
      <g class="phone-line">
        <rect class="icon-blue" x="18" y="164" width="15" height="23" rx="2"/>
        <rect class="fill-paper" x="21" y="168" width="9" height="14"/>
        <text class="phone-on-white" x="42" y="181">+0000 1234 5679</text>
      </g>

      <text class="holder-name" x="502" y="183" text-anchor="end">YOUR<tspan class="holder-name__last">NAME</tspan></text>

      <!-- address -->
      <g class="contact contact--address">
        <polygon class="icon-white" points="20,224 28,217 36,224 33,224 33,231 23,231 23,224"/>
        <text class="contact-text" x="20" y="252">Your Local or business</text>
        <text class="contact-text" x="20" y="268">address.</text>
      </g>

      <!-- phones -->
      <g class="contact contact--phones">
        <rect class="icon-white" x="190" y="222" width="14" height="9" rx="2"/>
        <rect class="icon-white" x="193" y="218" width="8" height="4" rx="1"/>
        <text class="contact-text" x="190" y="252">+000 1234 5679</text>
        <text class="contact-text" x="190" y="268">+000 1234 5679</text>
      </g>

      <!-- email / web -->
      <g class="contact contact--web">
        <rect class="icon-white" x="340" y="218" width="16" height="11" rx="1"/>
        <rect class="icon-white" x="345" y="230" width="6" height="3"/>
        <text class="contact-text" x="340" y="252">name@yourwebsite.com</text>
        <text class="contact-text" x="340" y="268">www.yourwebsite.com</text>
      </g>
    </svg>
  </div>

  <!-- Back side -->
  <div class="card card--back">
    <svg width="520" height="297" viewBox="0 0 520 297" xmlns="http://www.w3.org/2000/svg">
      <rect class="fill-paper" x="0" y="0" width="520" height="297"/>
      <rect class="fill-blue" x="0" y="0" width="232" height="8"/>
      <rect class="fill-black" x="236" y="0" width="284" height="8"/>
      <rect class="fill-black" x="0" y="289" width="284" height="8"/>
      <rect class="fill-blue" x="288" y="289" width="232" height="8"/>
      <text class="brand-name brand-name--on-white" x="260" y="160" text-anchor="middle">HARBOR RIDGE</text>
    </svg>
  </div>

</main>
</body>
</html>
```